Loom Harbor commercial brochure

We need a brochure that presents our services for commercial use. Without going into the details of our offers, that the prospect understands our added value and our expertise for the creation of a showcase site, e-commerce site and personalized, tailor-made application.

Please respect the graphic charter

Target Market(s)

Small and medium enterprises

Colors
F0912C
F2A743
F7CA91
FBE8D2
FDF5EE

Requirements
Must have
• a good presentation of our offers on several different pages
Nice to have
• little text but a lot of clarity and precision in the information
Should not have
• too much information, heavy design

```html
<!DOCTYPE html>
<html lang="en">
<head>
<meta charset="utf-8">
<title>Loom Harbor – Commercial Brochure</title>
<link rel="stylesheet" href="https://fonts.googleapis.com/css2?family=Quicksand:wght@400;500;600;700&display=swap">
<style>
  :root{
    --orange:#f24a0a;
    --orange-soft:#f7a27c;
    --peach:#fbe8d2;
    --paper:#ffffff;
    --paper-shade:#eeeeee;
    --ink:#3a3a3a;
    --ink-soft:#6b6b6b;
    --stage:#d6d6d6;
  }
  *{box-sizing:border-box;margin:0;padding:0}
  html,body{width:1200px;height:1200px;overflow:hidden}
  body{background:var(--stage);font-family:"Quicksand",sans-serif;color:var(--ink);position:relative}

  .spread{position:absolute;width:580px;height:205px;display:flex;box-shadow:0 6px 18px rgba(0,0,0,.18)}
  .spread--cover{left:15px;top:232px}
  .spread--agency{left:605px;top:232px}
  .spread--mobile{left:15px;top:497px}
  .spread--website{left:605px;top:497px}
  .spread--graphic{left:310px;top:762px}

  .page{position:relative;width:290px;height:205px;overflow:hidden;background:var(--paper)}
  .page--orange{background:var(--orange);color:#fff}

  .photo{position:absolute}
  .pattern{position:absolute}

  .brand{position:absolute;display:flex;align-items:center;gap:3px;font-weight:700;font-size:6px;color:var(--ink)}
  .brand::before{content:"";width:7px;height:7px;border-radius:50%;background:var(--orange)}
  .brand--light{color:#fff}
  .brand--light::before{background:#fff}
  .brand--large{font-size:11px;gap:6px}
  .brand--large::before{width:14px;height:14px}

  .folio{position:absolute;bottom:8px;font-size:4.5px;color:var(--ink-soft);letter-spacing:.3px}
  .folio b{color:var(--orange);font-weight:500}

  .title{font-weight:500;color:var(--orange);line-height:1.05}
  .body-copy{font-size:4.2px;line-height:1.45;color:var(--ink-soft)}

  /* cover */
  .cover-pattern{left:120px;top:20px;width:170px;height:185px;
    background:linear-gradient(135deg,rgba(255,255,255,0) 20%,rgba(255,255,255,.45) 60%,rgba(255,255,255,.8));
    clip-path:polygon(40% 0,100% 0,100% 100%,10% 100%)}
  .cover-brand{left:24px;top:92px}
  .contact{position:absolute;left:24px;top:128px;font-size:5.2px;line-height:1.6;font-style:normal}
  .contact__label{font-size:7px;text-decoration:underline;margin-bottom:2px;font-weight:500}
  .cover-photo{inset:0;background:linear-gradient(160deg,#d9d4cc 0%,#b9b3ab 35%,#8b8680 55%,#e8e6e3 80%,#f5f5f5 100%)}
  .cover-pattern-right{left:0;top:20px;width:90px;height:185px;
    background:linear-gradient(90deg,var(--orange) 0%,rgba(242,74,10,.55) 60%,rgba(242,74,10,0));
    clip-path:polygon(0 0,60% 0,100% 100%,0 100%)}
  .cover-flag{position:absolute;left:0;top:0;width:290px;height:205px}
  .cover-title{position:absolute;left:128px;top:28px;color:#fff;transform:rotate(-10deg);transform-origin:left top}
  .cover-title h1{font-size:15px;font-weight:500;letter-spacing:.6px}
  .cover-title p{font-size:5px;letter-spacing:.4px;margin-top:1px}
  .cover-brand-right{left:168px;top:160px}
  .cover-tagline{position:absolute;left:168px;top:176px;width:116px;font-size:4.6px;color:var(--ink)}

  /* agency */
  .agency-band{position:absolute;left:0;top:0;width:580px;height:72px;background:var(--orange);color:#fff;padding:14px 18px}
  .agency-band h2{font-size:13px;font-weight:500;letter-spacing:.6px}
  .agency-band p{font-size:4.2px;line-height:1.5;margin-top:5px;max-width:520px}
  .agency-photo{left:0;top:72px;width:580px;height:133px;background:linear-gradient(90deg,#e9e6e2 0%,#d8cfc6 30%,#c9c3bc 55%,#4a4a4e 80%,#2c2c30 100%)}
  .agency-pattern{left:440px;top:72px;width:140px;height:133px;background:linear-gradient(180deg,rgba(242,74,10,.6),rgba(255,255,255,.1));clip-path:polygon(40% 0,100% 0,100% 100%,0 100%)}
  .spread--agency .folio{color:#fff}

  /* mobile */
  .corner-band{position:absolute;left:0;top:0;width:290px;height:40px}
  .mobile-title{position:absolute;left:22px;top:26px;font-size:12px}
  .mobile-copy{position:absolute;left:22px;top:42px;width:230px}
  .stage-label{position:absolute;left:20px;bottom:18px;writing-mode:vertical-rl;transform:rotate(180deg);font-size:8px;color:var(--orange);font-weight:500}
  .steps{position:absolute;list-style:none}
  .steps li{display:flex;align-items:center;gap:6px;font-size:4.6px;letter-spacing:.3px;color:var(--ink-soft);height:20px}
  .steps li::before{content:"";width:8px;height:8px;border-radius:50%;background:var(--paper);box-shadow:0 1px 3px rgba(0,0,0,.25)}
  .mobile-steps{left:60px;top:98px}
  .mobile-photo{inset:0;background:linear-gradient(150deg,#e8c9bf 0%,#d6a59a 30%,#b89fb8 50%,#dcdcdc 75%,#f3f3f3 100%)}
  .mobile-pattern{right:0;bottom:0;width:120px;height:120px;background:linear-gradient(135deg,rgba(255,255,255,0),rgba(60,60,60,.35));clip-path:polygon(100% 0,100% 100%,0 100%)}
  .mobile-brand{left:60px;bottom:10px}

  /* website */
  .website-photo{inset:0;background:linear-gradient(170deg,#f2f2f2 0%,#e5e8ea 40%,#b98a5a 60%,#8f5f35 80%,#c7cdd3 100%)}
  .website-pattern{left:0;bottom:0;width:170px;height:70px;background:linear-gradient(0deg,rgba(255,255,255,.7),rgba(255,255,255,0));clip-path:polygon(0 0,100% 60%,100% 100%,0 100%)}
  .website-title{position:absolute;left:22px;top:18px;font-size:12px}
  .website-copy{position:absolute;left:22px;top:34px;width:230px}
  .website-steps{left:168px;top:62px}
  .website-steps li{flex-direction:column;align-items:flex-start;height:30px;gap:3px}
  .need-label{position:absolute;right:14px;top:30px;writing-mode:vertical-rl;font-size:7.5px;color:var(--orange);font-weight:500}
  .corner-br{position:absolute;right:0;bottom:0;width:290px;height:205px}
  .website-brand{left:22px;bottom:10px}

  /* graphic */
  .graphic-photo{inset:0;background:linear-gradient(180deg,#f4f4f4 0%,#ececec 45%,#e3e1de 70%,#d9c9b3 85%,#3aa9b8 100%)}
  .graphic-pattern{left:0;top:0;width:70px;height:120px;background:linear-gradient(180deg,var(--orange),rgba(242,74,10,0));clip-path:polygon(0 0,100% 0,0 100%)}
  .corner-tr{position:absolute;left:0;top:0;width:290px;height:205px}
  .graphic-title{position:absolute;left:28px;top:40px;font-size:10px;transform:rotate(-8deg);transform-origin:left top}
  .graphic-title span{display:block;font-size:6.5px;margin-top:1px}
  .graphic-copy{position:absolute;left:30px;top:65px;width:170px;transform:rotate(-8deg);transform-origin:left top}
  .universe-label{position:absolute;left:22px;bottom:22px;writing-mode:vertical-rl;transform:rotate(180deg);font-size:7px;color:var(--orange);font-weight:500;line-height:1.2}
  .services{position:absolute;left:90px;top:90px;width:170px;list-style:none}
  .services li{margin-bottom:6px}
  .services h3{font-size:5.2px;font-weight:600;color:var(--ink);margin-bottom:1.5px}
  .graphic-brand{left:90px;bottom:10px}
</style>
</head>
<body>

<section class="spread spread--cover">
  <div class="page page--orange">
    <div class="pattern cover-pattern" role="img" aria-label="Triangle mosaic pattern fading into the page"></div>
    <div class="brand brand--light brand--large cover-brand">Loom Harbor</div>
    <address class="contact">
      <div class="contact__label">CONTACT</div>
      18 Quay Lane 13002 Portside<br>
      06.41.52.63.74<br>
      04.91.20.30.40<br>
      contact@loomharbor.agency<br>
      www.loomharbor.agency
    </address>
  </div>
  <div class="page">
    <div class="photo cover-photo" role="img" aria-label="Photo of hands typing on a laptop at a bright desk"></div>
    <div class="pattern cover-pattern-right" role="img" aria-label="Triangle mosaic pattern continuing from the back cover"></div>
    <svg class="cover-flag" viewBox="0 0 290 205" aria-hidden="true">
      <polygon points="110,30 290,0 290,10 150,115" fill="var(--orange)"/>
    </svg>
    <div class="cover-title">
      <h1>THE AGENCY</h1>
      <p>TAKING YOU FROM IDEA TO SUCCESS</p>
    </div>
    <div class="brand cover-brand-right">Loom Harbor</div>
    <p class="cover-tagline">Tell us about your web project and we will give you the help you need.</p>
  </div>
</section>

<section class="spread spread--agency">
  <div class="page"></div>
  <div class="page"></div>
  <div class="photo agency-photo" role="img" aria-label="Photo of smiling colleagues meeting and shaking hands in an office"></div>
  <div class="pattern agency-pattern" role="img" aria-label="Triangle mosaic pattern over the photo"></div>
  <header class="agency-band">
    <h2>AN AGENCY CLOSE TO ITS CUSTOMERS</h2>
    <p>The agency develops with you an innovative and creative digital design, always at the service of your projects! At Loom Harbor, adaptability and innovation are the two keys to taking you from idea to success. Because each project is different and requires a precise understanding of your expectations and objectives, our development and creative team works in symbiosis to make your web and mobile projects a reality. A human-sized agency, Loom Harbor relies on proximity to customers and synergy between teams to develop a solution adapted to your expectations, together.</p>
  </header>
  <div class="folio" style="left:240px">PAGE <b>|</b> 01</div>
  <div class="folio" style="right:14px">PAGE <b>|</b> 02</div>
</section>

<section class="spread spread--mobile">
  <div class="page">
    <svg class="corner-band" viewBox="0 0 290 40" aria-hidden="true">
      <polygon points="0,0 80,0 0,30" fill="var(--orange)"/>
    </svg>
    <h2 class="title mobile-title">Mobile app</h2>
    <p class="body-copy mobile-copy">The creation of a mobile application is a strategic asset in terms of digital marketing. A mobile application is a differentiating tool for your offer and your project and a modern and innovative communication vector.<br>Discover the world of mobile at the fingertips of your web project.</p>
    <div class="stage-label">Your application in stages</div>
    <ul class="steps mobile-steps">
      <li>CONCEPTION</li>
      <li>DEVELOPMENT</li>
      <li>TEST &amp; VALIDATION</li>
      <li>LAUNCH</li>
    </ul>
    <div class="brand mobile-brand">Loom Harbor</div>
    <div class="folio" style="right:14px">PAGE <b>|</b> 01</div>
  </div>
  <div class="page">
    <div class="photo mobile-photo" role="img" aria-label="Photo of a hand tapping app icons on a smartphone"></div>
    <div class="pattern mobile-pattern" role="img" aria-label="Triangle mosaic pattern in the corner"></div>
    <div class="folio" style="right:14px">PAGE <b>|</b> 02</div>
  </div>
</section>

<section class="spread spread--website">
  <div class="page">
    <div class="photo website-photo" role="img" aria-label="Photo of a web design sketch on a wooden desk with a keyboard"></div>
    <div class="pattern website-pattern" role="img" aria-label="Triangle mosaic pattern along the bottom"></div>
    <div class="folio" style="right:14px">PAGE <b>|</b> 03</div>
  </div>
  <div class="page">
    <svg class="corner-br" viewBox="0 0 290 205" aria-hidden="true">
      <polygon points="290,120 290,205 250,205" fill="var(--orange-soft)"/>
      <polygon points="290,140 290,205 262,205" fill="var(--orange)"/>
      <polygon points="230,0 290,0 290,6" fill="var(--orange)"/>
    </svg>
    <h2 class="title website-title">Website</h2>
    <p class="body-copy website-copy">Loom Harbor creates a site in your image, adapted to your needs and allowing your project to stand out from the others. Depending on your objectives, our web agency accompanies you from idea to success!</p>
    <ul class="steps website-steps">
      <li>SHOWCASE SITE</li>
      <li>E-COMMERCE SITE</li>
      <li>TAILOR-MADE SITE</li>
    </ul>
    <div class="need-label">Your need your web solution</div>
    <div class="brand website-brand">Loom Harbor</div>
    <div class="folio" style="right:30px">PAGE <b>|</b> 04</div>
  </div>
</section>

<section class="spread spread--graphic">
  <div class="page">
    <div class="photo graphic-photo" role="img" aria-label="Photo of a whiteboard mind map about creativity above a desk with colour swatches and a cactus"></div>
    <div class="pattern graphic-pattern" role="img" aria-label="Triangle mosaic pattern in the top corner"></div>
    <div class="folio" style="right:14px">PAGE <b>|</b> 05</div>
  </div>
  <div class="page">
    <svg class="corner-tr" viewBox="0 0 290 205" aria-hidden="true">
      <polygon points="215,0 290,0 290,70" fill="var(--orange)"/>
    </svg>
    <h2 class="title graphic-title">Graphic design:<span>Your visual identity, your universe</span></h2>
    <p class="body-copy graphic-copy">Making your project shine and give it its colors is the objective and requirement of our communication and visual identity strategy, designed at your side and to lead you from idea to success!</p>
    <div class="universe-label">2 universes, 1 unique<br>visual image</div>
    <ul class="services">
      <li><h3>Website: from model to project</h3><p class="body-copy">The interface of your website meets a graphic and ergonomic requirement, to guarantee an effective user experience and respect for your visual identity.</p></li>
      <li><h3>Mobile app, UX Design as a priority</h3><p class="body-copy">Ergonomics, user experience and technical features are at the heart of the graphic work and layout of your mobile application.</p></li>
      <li><h3>Print, your signage identity</h3><p class="body-copy">Flyers, brochures, posters, banners, business cards, calendars... are all possible variations of your visual universe and your brand image.</p></li>
    </ul>
    <div class="brand graphic-brand">Loom Harbor</div>
    <div class="folio" style="right:14px">PAGE <b>|</b> 06</div>
  </div>
</section>

</body>
</html>
```